Farm Home Delivery Meat Box - Local Pasture Raised Meats

We need black and white box designs for 3 different box sizes for delivering our farms meat. We are looking to incorporate our logo, as well as our website and some other brand identity images. We are a farm that started a home delivery service delivering both the meat we raise, as well as other local goods such as cheese, vegetables, seafood and more.

Target Market(s)

Affluent families

Industry/Entity Type

Agriculture

Font styles to use
Other font styles liked:
• Sheepman Regular

Colors

Designer to choose only greyscale colors for use in the design.

Requirements
Must have
• Must be black and white, would like a nice crisp modern look to it. Can incorporate farm animals or farm look in addition. Must have the attached logo in it as well as our "brand"-the BKA. Any other modern farm look, or slogan incorporated as well would be good. Should lastly have our website, BirchKnollAcres.example Utilizing the entire box besides the bottom.
Nice to have
• Gave an example of box design I like. Also template for size reference-Disregard the logo in it.

```html
<!DOCTYPE html>
<html lang="en">
<head>
<meta charset="utf-8">
<title>Birch Knoll Acres – Delivery Box Panels</title>
<link href="https://fonts.googleapis.com/css2?family=Courier+Prime:wght@400;700&display=swap" rel="stylesheet">
<style>
  :root {
    --stage: #ededed;
    --board-dark: #3b3b3d;
    --board-darker: #2f2f31;
    --board-light: #f7f7f5;
    --ink-dark: #2b2b2b;
    --ink-mid: #555555;
    --ink-light: #f2f2f2;
    --rule: #9a9a9a;
    --art-tone: #d9d9d9;
  }
  * { box-sizing: border-box; margin: 0; padding: 0; }
  html, body { width: 1200px; height: 1000px; overflow: hidden; }
  body {
    background: var(--stage);
    font-family: "Courier Prime", "Courier New", monospace;
    color: var(--ink-dark);
    position: relative;
  }

  /* Lid panel */
  .lid {
    position: absolute; left: 40px; top: 300px;
    width: 380px; height: 400px;
    background: var(--board-dark);
  }
  .lid-mark {
    position: absolute; left: 50%; top: 150px; transform: translate(-50%, -50%);
    width: 230px; height: 230px; border-radius: 50%;
    border: 2px solid var(--ink-light);
    display: flex; align-items: center; justify-content: center;
  }
  .brand-name {
    font-weight: 700; text-transform: uppercase; text-align: center;
    color: var(--ink-light); letter-spacing: 1px; line-height: 1.1;
  }
  .lid-mark .brand-name { font-size: 26px; }
  .lid-band {
    position: absolute; left: 0; right: 0; top: 300px; height: 58px;
    background: var(--board-light); text-align: center; padding-top: 6px;
  }
  .band-kicker { font-size: 13px; color: var(--ink-mid); }
  .band-headline { font-size: 19px; letter-spacing: 0.5px; }
  .lid-url {
    position: absolute; left: 0; right: 0; top: 368px;
    text-align: center; font-size: 10px; color: var(--ink-light); letter-spacing: 1px;
  }

  /* Side panel */
  .side {
    position: absolute; left: 460px; top: 300px;
    width: 700px; height: 400px; display: flex;
  }
  .side-main {
    position: relative; width: 380px; background: var(--board-light);
  }
  .side-band-top {
    position: absolute; left: 0; right: 0; top: 0; height: 68px;
    border-bottom: 1px solid var(--rule);
    text-align: center; padding-top: 8px;
  }
  .side-band-top .band-kicker { font-size: 12px; }
  .side-band-top .band-headline { font-size: 17px; }
  .band-url { font-size: 9px; color: #666; letter-spacing: 1px; }
  .side-mark {
    position: absolute; left: 22px; top: 92px;
    display: flex; align-items: center; gap: 8px;
  }
  .side-mark .dot { width: 16px; height: 16px; border-radius: 50%; border: 2px solid var(--ink-dark); }
  .side-mark .brand-name { color: var(--ink-dark); font-size: 15px; }
  .belief {
    position: absolute; left: 22px; top: 180px; width: 200px;
    font-size: 15px; line-height: 1.2;
  }
  .animal-art {
    position: absolute; left: 230px; top: 270px; width: 150px; height: 130px;
    background: linear-gradient(180deg, var(--board-light), var(--art-tone));
  }
  .side-strip {
    position: relative; width: 100px; background: var(--board-darker);
  }
  .handles {
    position: absolute; left: 8px; top: 24px; font-size: 9px; color: var(--ink-light);
    line-height: 2; white-space: nowrap;
  }
  .side-strip-light { width: 20px; background: var(--board-light); border-left: 1px solid var(--rule); }
  .side-end {
    position: relative; flex: 1; background: var(--board-dark);
  }
  .side-end-url {
    position: absolute; left: 0; right: 0; top: 300px; text-align: center;
    font-size: 11px; color: var(--ink-light); letter-spacing: 0.4px; white-space: nowrap;
  }
</style>
</head>
<body>
  <section class="lid">
    <div class="lid-mark"><p class="brand-name">Birch Knoll<br>Acres</p></div>
    <div class="lid-band">
      <p class="band-kicker">Pasture Raised Meats</p>
      <p class="band-headline">Delivered to your Door</p>
    </div>
    <p class="lid-url">www.birchknollacres.example</p>
  </section>

  <section class="side">
    <div class="side-main">
      <div class="side-band-top">
        <p class="band-kicker">Pasture Raised Meats</p>
        <p class="band-headline">Delivered to your Door</p>
        <p class="band-url">www.birchknollacres.example</p>
      </div>
      <div class="side-mark"><span class="dot"></span><p class="brand-name">Birch Knoll Acres</p></div>
      <p class="belief">We believe in community, food raised with integrity, and being good stewards of the land.</p>
      <div class="animal-art" role="img" aria-label="Line illustration of a cow, a rooster and a pig"></div>
    </div>
    <div class="side-strip">
      <p class="handles">BirchKnollAcres<br>BirchKnollAcres</p>
    </div>
    <div class="side-strip-light"></div>
    <div class="side-end"><p class="side-end-url">www.birchknollacres.example</p></div>
  </section>
</body>
</html>
```